BrawnCrate placard

I need a placard designed that will go in my monthly subscription boxes to describe the products inside. There must be space to write 3-5 sentences on each product.
the first area will be titled: For your flowing mane
2 for your macho glow
3 to keep you smelling macho
4 to keep you clanging and banging at the gym.
Placard will be 5inchs wide and 7inchs long

I have attached the logo and the website address must be used in the design brawncrates.com.

Target Market(s)

men between 20-50

Colors

Designer to choose colors to be used in the design.

Requirements
Must have
• My website address brawncrates.com
• 4 area to write 3-5 sentences
• 1 for your flowing mane
• 2to keep you smelling macho
• 3 to keep you clanging and banging at the gym
• 4 for your macho glow

```html
<!DOCTYPE html>
<html lang="en">
<head>
<meta charset="utf-8">
<title>BrawnCrate Placard</title>
<link rel="stylesheet" href="https://fonts.googleapis.com/css2?family=Michroma&family=Orbitron:wght@700;800&family=Oswald:wght@500&family=Questrial&display=swap">
<style>
  :root {
    --backdrop: #111111;
    --navy: #151a26;
    --red: #e31b23;
    --wood-light: #f2f2f2;
    --wood-grey: #c9c9c9;
    --white: #ffffff;
    --ink: #111111;
    --body-text: #e8e8ec;
  }
  * { margin: 0; padding: 0; box-sizing: border-box; }
  html, body {
    width: 1200px; height: 1200px; overflow: hidden;
    background: var(--backdrop);
  }
  .placard {
    position: absolute; left: 238px; top: 94px;
    width: 904px; height: 1265px;
    transform: scale(0.8); transform-origin: top left;
    background: var(--navy); overflow: hidden;
    font-family: "Questrial", sans-serif;
  }
  .wood-backdrop {
    position: absolute; left: 0; top: 0; width: 904px; height: 600px;
    background: linear-gradient(90deg, var(--wood-grey) 0%, var(--wood-light) 8%, var(--white) 50%, var(--wood-light) 92%, var(--wood-grey) 100%);
  }
  .chevron-bands { position: absolute; left: 0; top: 0; width: 904px; height: 1265px; }
  .portrait-photo {
    position: absolute; left: 362px; top: 10px; width: 542px; height: 700px;
    background: linear-gradient(180deg, #2a2a2e 0%, #1b1e28 45%, var(--navy) 100%);
    clip-path: polygon(0 700px, 0 470px, 30px 330px, 60px 240px, 160px 200px, 150px 60px, 230px 5px, 340px 5px, 400px 70px, 420px 200px, 542px 300px, 542px 700px);
  }
  .product-box-photo {
    position: absolute; left: 62px; top: 323px; width: 330px; height: 360px;
    background: linear-gradient(160deg, #fbfbfb 0%, #e2e2e2 55%, #bdbdbd 100%);
    clip-path: polygon(0 30%, 52% 0, 100% 25%, 100% 75%, 42% 100%, 5% 68%);
  }
  .brand-name {
    position: absolute; left: 82px; top: 258px; width: 300px;
    font-family: "Michroma", sans-serif; font-size: 31px; color: var(--red);
    text-align: center; white-space: nowrap;
  }
  .brand-tagline {
    position: absolute; left: 82px; top: 302px; width: 300px;
    font-family: "Oswald", sans-serif; font-weight: 500; font-size: 10px;
    color: var(--ink); text-align: center; white-space: nowrap;
  }
  .product-note { position: absolute; width: 410px; }
  .product-note .icon-slot {
    position: absolute; width: 46px; height: 72px;
    background: var(--white); border-radius: 22px 22px 18px 18px;
  }
  .product-note h2 {
    font-family: "Orbitron", sans-serif; font-weight: 800; font-size: 17px;
    color: var(--red); line-height: 21px; text-transform: uppercase;
    margin-bottom: 4px; white-space: nowrap;
  }
  .product-note p { font-size: 13.5px; line-height: 15px; color: var(--body-text); white-space: nowrap; }
  .note-mane { left: 47px; top: 796px; }
  .note-scent { left: 484px; top: 796px; }
  .note-gym { left: 47px; top: 994px; }
  .note-glow { left: 484px; top: 994px; }
  .product-note .icon-slot { left: 128px; top: -94px; }
  .call-line {
    position: absolute; left: 0; top: 1194px; width: 904px; text-align: center;
    font-family: "Orbitron", sans-serif; font-weight: 800; font-size: 23px;
    color: var(--ink); white-space: nowrap;
  }
  .web-line {
    position: absolute; left: 0; top: 1226px; width: 904px; text-align: center;
    font-family: "Orbitron", sans-serif; font-weight: 700; font-size: 16px;
    color: var(--white); letter-spacing: 12px; white-space: nowrap;
  }
</style>
</head>
<body>
  <main class="placard">
    <div class="wood-backdrop" role="img" aria-label="Weathered white wooden plank background"></div>
    <svg class="chevron-bands" viewBox="0 0 904 1265" aria-hidden="true">
      <polygon points="0,391 452,573 904,391 904,1265 0,1265" fill="var(--red)"/>
      <polygon points="0,423 452,601 904,423 904,1265 0,1265" fill="var(--navy)"/>
      <polygon points="0,1131 452,1181 904,1131 904,1265 0,1265" fill="#dfe6ee"/>
      <polygon points="0,1138 452,1188 904,1138 904,1265 0,1265" fill="var(--red)"/>
    </svg>
    <div class="portrait-photo" role="img" aria-label="Photo of a bearded man in a dark suit lowering his sunglasses"></div>
    <div class="product-box-photo" role="img" aria-label="Photo of a white BrawnCrate gift box"></div>

    <div class="brand-name">BrawnCrate</div>
    <div class="brand-tagline">MENS GROOMING AND ESSENTIALS FOR THE EVERYDAY MACHO MAN</div>

    <section class="product-note note-mane">
      <div class="icon-slot" role="img" aria-label="Bearded man icon"></div>
      <h2>For your flowing mane</h2>
      <p>Lorem ipsum dolor sit amet, consectetur adipiscing elit, sed<br>do eiusmod tempor incididunt ut labore et dolore magna<br>aliqua. Ut enim ad minim veniam, quis nostrud exercitation<br>ullamco laboris nisi ut aliquip ex.</p>
    </section>
    <section class="product-note note-scent">
      <div class="icon-slot" role="img" aria-label="Bearded man with glasses icon"></div>
      <h2>To keep you smelling macho</h2>
      <p>Lorem ipsum dolor sit amet, consectetur adipiscing elit, sed<br>do eiusmod tempor incididunt ut labore et dolore magna<br>aliqua. Ut enim ad minim veniam, quis nostrud exercitation<br>ullamco laboris nisi ut aliquip ex.</p>
    </section>
    <section class="product-note note-gym">
      <div class="icon-slot" role="img" aria-label="Man with sunglasses and moustache icon"></div>
      <h2>To keep you clanging and<br>banging at the gym</h2>
      <p>Lorem ipsum dolor sit amet, consectetur adipiscing elit, sed do<br>eiusmod tempor incididunt ut labore et dolore magna aliqua. Ut<br>enim ad minim veniam, quis nostrud exercitation ullamco laboris<br>nisi ut aliquip ex.</p>
    </section>
    <section class="product-note note-glow">
      <div class="icon-slot" role="img" aria-label="Bearded man with sunglasses icon"></div>
      <h2>For your macho glow</h2>
      <p>Lorem ipsum dolor sit amet, consectetur adipiscing elit, sed<br>do eiusmod tempor incididunt ut labore et dolore magna<br>aliqua. Ut enim ad minim veniam, quis nostrud exercitation<br>ullamco laboris nisi ut aliquip ex.</p>
    </section>

    <div class="call-line">Call BrawnCrate toll free 1-800-555-0147</div>
    <div class="web-line">www.brawncrates.com</div>
  </main>
</body>
</html>
```